A DL (210mm wide x 100mm deep) layered .psd prepared for print ready CMYK 300 dpi for gloss paper.

Target Market(s)

Business People & young professionals – middle – high income earners.

Requirements
Must have
• Heading:
TOP Brunch (big and bold)
Trade Owners People (smaller underneath)

Text:
Everything about the TOP Brunch is TOP. The TOP Brunches are aimed at Trade, Owners and People and are designed to be an environment for where people Thrive, Own and Prosper, while learning Trade, Openness and Principle.

These events will be held on Friday mornings at 7am on February 17, May 18, August 17 and November 16, 2012.

The Marlow Playhouse, 412 Penrose Avenue, Newcastle.
For more information, Phone (02) 4631 5702 or email info@chapel240.example

Please include:
SFP Logo, Chapel240 Logo, & TOP Logo
Nice to have
• Open to blue colours refer to steadyfundplanning.example and Chapel240.example

- Open to graphics/illustrations/photos - Can also purchase images from PixVault.
Should not have
• Too Much Bright Red or Yellow (open to some but not like a Grillcorns flyer)

```html
<!DOCTYPE html>
<html lang="en">
<head>
<meta charset="utf-8">
<title>TOP Brunch – DL Flyer</title>
<link rel="stylesheet" href="https://fonts.googleapis.com/css2?family=Cinzel:wght@400;700&family=Crimson+Text:ital,wght@0,400;0,600;0,700;1,400;1,600&display=swap">
<style>
  :root{
    --page:#ffffff;
    --navy:#3d5a7c;
    --navy-deep:#2b4563;
    --navy-light:#6f8fb3;
    --paper:#ffffff;
    --paper-shade:#e6e9ee;
    --ink:#4b6685;
    --rule:#8da2bb;
    --partner-grey:#6a6a6a;
    --partner-blue:#3e6fb8;
    --white:#ffffff;
  }
  *{box-sizing:border-box;margin:0;padding:0}
  html,body{width:1200px;height:1200px;overflow:hidden;background:var(--page)}
  .flyer{
    position:absolute;left:80px;top:345px;width:1053px;height:500px;overflow:hidden;
    background:radial-gradient(ellipse 320px 300px at 200px 240px,var(--navy-light) 0%,var(--navy) 55%,var(--navy-deep) 100%);
  }
  .flyer__strip{
    position:absolute;inset:0;
    background:linear-gradient(90deg,transparent 960px,var(--navy) 1000px,var(--navy-deep) 1053px);
  }
  .flyer__panel{
    position:absolute;inset:0;
    background:linear-gradient(100deg,var(--paper) 0%,var(--paper) 45%,var(--paper-shade) 75%,var(--paper) 100%);
    clip-path:polygon(412px 0,1053px 0,1053px 135px,1023px 500px,373px 500px);
  }
  .brand{position:absolute;left:0;top:0;width:400px;height:500px;color:var(--white);text-align:center}
  .brand__name{
    position:absolute;left:30px;top:150px;width:345px;
    font-family:"Crimson Text",serif;font-weight:700;font-size:124px;line-height:1;letter-spacing:2px;
  }
  .brand__tagline{
    position:absolute;left:30px;top:293px;width:345px;
    font-family:"Crimson Text",serif;font-weight:600;font-size:19px;line-height:24px;text-transform:uppercase;
  }
  .brand__event{
    position:absolute;left:30px;top:358px;width:345px;
    font-family:"Cinzel",serif;font-size:44px;line-height:56px;letter-spacing:1px;
  }
  .photos{position:absolute;top:0;left:435px;display:flex;gap:3px}
  .photos__item{height:135px}
  .photos__item--one{width:187px;background:linear-gradient(160deg,#7fb6e4,#cfe3f2 55%,#b8a3c9)}
  .photos__item--two{width:180px;background:linear-gradient(150deg,#c9472f,#4f7fb0 55%,#d9b28f)}
  .photos__item--three{width:184px;background:linear-gradient(160deg,#e9ecef,#d8b89a 50%,#6e7d93)}
  .details{font-family:"Crimson Text",serif;color:var(--ink);text-align:center}
  .details__block{position:absolute;left:436px;width:560px}
  .details__intro{top:155px;font-style:italic;font-size:17.5px;line-height:25px}
  .details__dates{top:291px;font-size:19px;line-height:25px;font-variant:small-caps;letter-spacing:0.3px}
  .details__venue{top:363px;font-style:italic;font-size:17.5px;line-height:25px}
  .details__venue strong{font-weight:600}
  .rule{position:absolute;left:500px;width:432px;height:12px}
  .rule--upper{top:261px}
  .rule--lower{top:344px}
  .rule::before{content:"";position:absolute;left:0;right:0;top:5px;border-top:1px dashed var(--rule)}
  .rule::after{content:"";position:absolute;left:50%;top:2px;width:7px;height:7px;margin-left:-3.5px;border-radius:50%;background:var(--ink)}
  .partner{
    position:absolute;top:450px;width:200px;text-align:center;
    font-family:"Crimson Text",serif;font-weight:600;font-size:23px;line-height:30px;
  }
  .partner--sfp{left:480px;color:var(--partner-grey)}
  .partner--chapel{left:707px;color:var(--partner-blue)}
</style>
</head>
<body>
  <section class="flyer">
    <div class="flyer__strip"></div>
    <div class="flyer__panel"></div>

    <header class="brand">
      <div class="brand__name">TOP</div>
      <div class="brand__tagline">Trade Owners People</div>
      <div class="brand__event">Brunch</div>
    </header>

    <div class="photos">
      <div class="photos__item photos__item--one" role="img" aria-label="Photo of a smiling young woman with arms outstretched by the sea"></div>
      <div class="photos__item photos__item--two" role="img" aria-label="Photo of a cheerful group of young friends celebrating"></div>
      <div class="photos__item photos__item--three" role="img" aria-label="Photo of young professionals smiling and giving thumbs up"></div>
    </div>

    <div class="details">
      <p class="details__block details__intro">Everything about the TOP Brunch is TOP. The TOP Brunches are aimed at Trade, Owners and People and are designed to be an environment for where people Thrive, Own and Prosper, while learning Trade, Openness and Principle.</p>
      <div class="rule rule--upper"></div>
      <p class="details__block details__dates">These events will be held on Friday mornings at 7am<br>on February 17, May 18, August 17 and November 16, 2012.</p>
      <div class="rule rule--lower"></div>
      <p class="details__block details__venue">The Marlow Playhouse, 412 Penrose Avenue, Newcastle.<br>For more information, Phone <strong>(02) 4631 5702</strong> or email <strong>info@chapel240.example</strong></p>
    </div>

    <span class="partner partner--sfp">SFP</span>
    <span class="partner partner--chapel">Chapel240</span>
  </section>
</body>
</html>
```